Gentleman's grooming products require a business card

I need a business card that incorporates the logo [ or parts of ] that we had Pixel Hive design for us as uploaded.

We sell online, mens grooming products including moustache waxes, beard oils and shaving accessories.
We want a card that is classy, professional and a card that shouts mens products.

Target Market(s)

Young professional male market

Industry/Entity Type

Business

Contact Information for Business Card

Ross and Edith Carwell
Lather and Lore
Purveyors of gentleman's stiffeners and grooming requisites
M :0418529647
E : ross@latherandlore.com.au
E : edith@latherandlore.com.au
E : sales@theblokesbalmery.com.au

W : www.latherandlore.com.au

Requirements
Must have
• Class
Nice to have
• Professionalism

```html
<!DOCTYPE html>
<html lang="en">
<head>
<meta charset="utf-8">
<title>Lather and Lore — Business Card</title>
<link rel="stylesheet" href="https://fonts.googleapis.com/css2?family=Noto+Serif:wght@400&family=Marcellus&display=swap">
<style>
  :root {
    --backdrop: #e9e4dc;
    --card: #0b0b0b;
    --ink: #f2f2f2;
    --ink-soft: #dcdcdc;
    --rule: #cfcfcf;
  }
  * { margin: 0; padding: 0; box-sizing: border-box; }
  html, body {
    width: 1000px; height: 1200px; overflow: hidden;
    background: var(--backdrop);
  }
  .stage { position: relative; width: 1000px; height: 1200px; }
  .card {
    position: absolute; left: 90px; width: 818px; height: 505px;
    background: linear-gradient(135deg, #141414 0%, var(--card) 60%, #080808 100%);
    color: var(--ink);
    font-family: "Noto Serif", Georgia, serif;
    box-shadow: 0 6px 14px rgba(0,0,0,.35);
  }
  .card--front { top: 76px; }
  .card--second { top: 625px; }

  .brand-mark {
    position: absolute; left: 363px; top: 49px; width: 118px; height: 110px;
    border: 2px solid var(--ink);
  }
  .brand-rule {
    position: absolute; left: 178px; width: 488px; height: 2px; background: var(--ink);
  }
  .brand-rule--top { top: 160px; }
  .brand-rule--bottom { top: 270px; }
  .brand-name {
    position: absolute; left: 178px; width: 488px; top: 180px;
    text-align: center; font-size: 52px; font-weight: 400; line-height: 80px;
    color: var(--ink); white-space: nowrap;
  }
  .tagline {
    position: absolute; left: 170px; width: 504px; top: 277px;
    text-align: center; font-family: "Marcellus", Georgia, serif;
    font-size: 11.5px; letter-spacing: 1.2px; color: var(--ink-soft); white-space: nowrap;
  }

  .contact { position: absolute; left: 48px; top: 338px; list-style: none; }
  .contact li { display: flex; align-items: center; gap: 9px; font-size: 17px; line-height: 26px; white-space: nowrap; }
  .contact li.contact__phone { font-size: 21px; line-height: 30px; gap: 10px; }
  .contact svg { flex: none; }

  .owners { position: absolute; right: 40px; top: 339px; text-align: right; white-space: nowrap; }
  .owners__names { font-size: 21px; line-height: 30px; }
  .owners__role { font-size: 17px; line-height: 22px; color: var(--ink-soft); }

  .web {
    position: absolute; left: 52px; right: 40px; top: 467px;
    display: flex; align-items: center; gap: 14px; font-size: 17px; line-height: 24px; white-space: nowrap;
  }
  .web::before, .web::after { content: ""; flex: 1; height: 1.5px; background: var(--rule); }
</style>
</head>
<body>
<main class="stage">
  <article class="card card--front">
    <div class="brand-mark"></div>
    <div class="brand-rule brand-rule--top"></div>
    <div class="brand-name">Lather and Lore</div>
    <div class="brand-rule brand-rule--bottom"></div>
    <p class="tagline">MAKERS OF FINE BEARD OILS, MOUSTACHE WAXES AND SHAVING GOODS</p>
    <ul class="contact">
      <li class="contact__phone">
        <svg width="16" height="22" viewBox="0 0 16 22"><rect x="1" y="1" width="14" height="20" rx="2" fill="none" stroke="#f2f2f2" stroke-width="2"/><rect x="4" y="4" width="8" height="5" fill="#f2f2f2"/><rect x="4" y="11" width="8" height="7" fill="#f2f2f2"/></svg>0418529647</li>
      <li><svg width="17" height="12" viewBox="0 0 17 12"><rect x="0.5" y="0.5" width="16" height="11" fill="#f2f2f2"/><path d="M1 1 L8.5 7 L16 1 M1 11 L6 6 M16 11 L11 6" stroke="#0b0b0b" stroke-width="1.3" fill="none"/></svg>ross@latherandlore.com.au</li>
      <li><svg width="17" height="12" viewBox="0 0 17 12"><rect x="0.5" y="0.5" width="16" height="11" fill="#f2f2f2"/><path d="M1 1 L8.5 7 L16 1 M1 11 L6 6 M16 11 L11 6" stroke="#0b0b0b" stroke-width="1.3" fill="none"/></svg>edith@latherandlore.com.au</li>
      <li><svg width="17" height="12" viewBox="0 0 17 12"><rect x="0.5" y="0.5" width="16" height="11" fill="#f2f2f2"/><path d="M1 1 L8.5 7 L16 1 M1 11 L6 6 M16 11 L11 6" stroke="#0b0b0b" stroke-width="1.3" fill="none"/></svg>sales@theblokesbalmery.com.au</li>
    </ul>
    <div class="owners">
      <p class="owners__names">Ross and Edith Carwell</p>
      <p class="owners__role">Owners</p>
    </div>
    <p class="web">www.latherandlore.com.au</p>
  </article>

  <article class="card card--second">
    <div class="brand-mark"></div>
    <div class="brand-rule brand-rule--top"></div>
    <div class="brand-name">Lather and Lore</div>
    <div class="brand-rule brand-rule--bottom"></div>
    <p class="tagline">MAKERS OF FINE BEARD OILS, MOUSTACHE WAXES AND SHAVING GOODS</p>
    <ul class="contact">
      <li class="contact__phone">
        <svg width="16" height="22" viewBox="0 0 16 22"><rect x="1" y="1" width="14" height="20" rx="2" fill="none" stroke="#f2f2f2" stroke-width="2"/><rect x="4" y="4" width="8" height="5" fill="#f2f2f2"/><rect x="4" y="11" width="8" height="7" fill="#f2f2f2"/></svg>0418529647</li>
      <li><svg width="17" height="12" viewBox="0 0 17 12"><rect x="0.5" y="0.5" width="16" height="11" fill="#f2f2f2"/><path d="M1 1 L8.5 7 L16 1 M1 11 L6 6 M16 11 L11 6" stroke="#0b0b0b" stroke-width="1.3" fill="none"/></svg>ross@latherandlore.com.au</li>
      <li><svg width="17" height="12" viewBox="0 0 17 12"><rect x="0.5" y="0.5" width="16" height="11" fill="#f2f2f2"/><path d="M1 1 L8.5 7 L16 1 M1 11 L6 6 M16 11 L11 6" stroke="#0b0b0b" stroke-width="1.3" fill="none"/></svg>edith@latherandlore.com.au</li>
      <li><svg width="17" height="12" viewBox="0 0 17 12"><rect x="0.5" y="0.5" width="16" height="11" fill="#f2f2f2"/><path d="M1 1 L8.5 7 L16 1 M1 11 L6 6 M16 11 L11 6" stroke="#0b0b0b" stroke-width="1.3" fill="none"/></svg>sales@theblokesbalmery.com.au</li>
    </ul>
    <div class="owners">
      <p class="owners__names">Ross and Edith Carwell</p>
      <p class="owners__role">Owners</p>
    </div>
    <p class="web">www.latherandlore.com.au</p>
  </article>
</main>
</body>
</html>
```